web Design for Architecture and Interior Design Firm

This is a complete redesign of an architecture and interior design firm.( http://www.tqworkshop.com )
We have established a new look-n-feel for them and need to apply it to the new site/new architecture. Wireframes attached with logo and PDF of new brochure.
This will require a quck turn-around. The client is expecting a very modern design with web 2.0 in mind.
Again very quick turn-around! If you cannot commit to a Friday deliverable, do not bid! Must be completed by no later than Friday!

```html
<!DOCTYPE html>
<html lang="en">
<head>
<meta charset="utf-8">
<title>Tessaro Quinn Design Studios</title>
<link rel="stylesheet" href="https://fonts.googleapis.com/css2?family=Jost:wght@300;400&family=Arimo:wght@400;700&display=swap">
<style>
:root{
  --brown:#5e5445;
  --brown-dark:#4a4134;
  --red:#c8102e;
  --red-bg:#c41a35;
  --white:#ffffff;
  --text:#333333;
  --heading:#5b5244;
  --rule:#8a8a8a;
  --input-border:#9a9a9a;
}
*{margin:0;padding:0;box-sizing:border-box}
html,body{width:1200px;height:1014px;overflow:hidden}
body{position:relative;background:var(--red-bg);font-family:"Arimo",Arial,sans-serif;color:var(--text)}
.backdrop-top{position:absolute;left:0;top:0;width:1200px;height:564px;background:linear-gradient(#6b604f 0%,#5a5042 30%,#2a2520 60%,#000 78%)}
.backdrop-pattern{position:absolute;left:0;top:606px;width:1200px;height:408px;background:linear-gradient(135deg,#c81a36,#b8162f 60%,#c41f3a)}
.caption-band{position:absolute;left:0;top:564px;width:1200px;height:42px;background:var(--brown)}
.caption-band .caption{position:absolute;left:841px;top:0;height:26px;border-left:1px solid var(--white);padding-left:10px;padding-top:9px;font-family:"Jost",sans-serif;font-weight:300;font-size:19px;color:var(--white);line-height:20px}
.header{position:absolute;left:159px;top:0;width:882px;height:118px;background:var(--white)}
.brand{position:absolute;left:62px;top:40px;display:flex;flex-direction:column;align-items:center}
.brand .name{font-family:"Jost",sans-serif;font-weight:400;font-size:31px;color:var(--brown);letter-spacing:-0.5px;line-height:32px;display:flex;align-items:center;gap:6px}
.brand .name i{display:inline-block;width:10px;height:10px;background:var(--red)}
.brand .tag{font-family:"Jost",sans-serif;font-weight:400;font-size:14px;color:var(--brown);margin-top:4px;border-top:1px solid #bbb;padding-top:2px}
.nav{position:absolute;left:405px;top:69px;display:flex;font-family:"Jost",sans-serif;font-weight:400;font-size:12.5px;color:#3c352c;letter-spacing:-0.2px}
.nav a{color:inherit;text-decoration:none}
.nav a.active{color:var(--red)}
.nav span{margin:0 12px;color:#777}
.hero{position:absolute;left:159px;top:118px;width:882px;height:446px;background:linear-gradient(180deg,#c9c3b8 0%,#3a3634 28%,#2c2a2a 55%,#d98a3a 75%,#5a5a5e 100%)}
.slider-next{position:absolute;left:1012px;top:390px;width:29px;height:29px;background:#000}
.content{position:absolute;left:159px;top:606px;width:882px;height:408px;background:var(--white)}
.intro{position:absolute;left:43px;top:27px;width:520px}
.intro h1{font-size:22.5px;font-weight:700;color:var(--heading);line-height:27px;margin-bottom:15px}
.intro p{font-size:11.4px;line-height:16px;color:var(--text);margin-bottom:16px}
.side{position:absolute;left:613px;top:29px;width:240px}
.side h2{font-family:"Jost",sans-serif;font-weight:400;font-size:15px;color:var(--heading);letter-spacing:0.3px}
.post{margin-top:0}
.post h3{font-size:10.5px;font-weight:400;color:var(--red);line-height:13px}
.post p{font-size:10.2px;line-height:12px;color:#444}
.post a{color:#222;text-decoration:underline}
.blog h2{margin-bottom:13px}
.blog .post+.post{margin-top:11px}
.newsletter{position:absolute;left:613px;top:197px}
.newsletter h2{margin-bottom:13px}
.field{display:flex;align-items:center;margin-bottom:16px;font-size:10.5px}
.field label{width:42px}
.field .box{width:153px;height:18px;border:1px solid var(--input-border);background:#fff}
.actions{display:flex;gap:10px;margin-left:42px;margin-top:2px}
.btn{width:70px;height:23px;border:1px solid #999;border-radius:3px;background:linear-gradient(#f4f4f4,#c9c9c9);font-size:10.5px;color:#222;display:flex;align-items:center;justify-content:center}
.footer{position:absolute;left:30px;top:362px;width:825px;border-top:1px solid var(--rule);padding-top:14px;display:flex;justify-content:space-between;font-size:10.2px;color:#444}
.follow{display:flex;align-items:center;gap:5px}
.follow i{display:inline-block;width:10px;height:10px;background:#555}
</style>
</head>
<body>
<div class="backdrop-top"></div>
<div class="backdrop-pattern" role="img" aria-label="Red background with faint architectural floor plan drawing"></div>
<div class="caption-band"><div class="caption">Harbor Media Office</div></div>

<header class="header">
  <div class="brand">
    <div class="name">Tessaro Quinn <i></i></div>
    <div class="tag">spaces built around people</div>
  </div>
  <nav class="nav">
    <a class="active" href="#">HOME</a><span>|</span>
    <a href="#">ABOUT US</a><span>|</span>
    <a href="#">SERVICES</a><span>|</span>
    <a href="#">PORTFOLIO</a><span>|</span>
    <a href="#">CAREER</a><span>|</span>
    <a href="#">CONTACT US</a>
  </nav>
</header>

<div class="hero" role="img" aria-label="Photo of a meeting room with a white table, orange chairs and a wall of circular graphic panels"></div>
<div class="slider-next"></div>

<main class="content">
  <section class="intro">
    <h1>Tessaro Quinn Design Studios Makes the Process Predictable</h1>
    <p>When something as important as the very space in which your business lives and works is about to be disrupted, you should be confident you've chosen the right space and the best team to ensure a successful project. Rely on Tessaro-Quinn Design Studios to meet your needs and to make the process predictable. You can be assured that your project goals and objectives will be achieved.</p>
    <p>Rely on Tessaro-Quinn Design Studios to meet your needs and to make the process predictable. You can be assured that your project goals and objectives will be achieved. When something as important as the very space in which your business lives and works is about to be disrupted, you should be confident you've chosen the right space and the best team to ensure a successful project.</p>
  </section>

  <aside class="side blog">
    <h2>BLOG</h2>
    <div class="post">
      <h3>Blog Title 1</h3>
      <p>Lorem ipsum dolor sit amet, consectetur adipisc-ing elit. Mauris vitae dui nunc. Nullam lacus lacus...<a href="#">more</a></p>
    </div>
    <div class="post">
      <h3>Blog Title 2</h3>
      <p>Lorem ipsum dolor sit amet, consectetur adipisc-ing elit. Mauris vitae dui nunc. Nullam lacus lacus...<a href="#">more</a></p>
    </div>
  </aside>

  <section class="newsletter">
    <h2>NEWSLETTER</h2>
    <div class="field"><label>Name</label><div class="box"></div></div>
    <div class="field"><label>Email</label><div class="box"></div></div>
    <div class="actions"><div class="btn">Subscribe</div><div class="btn">Unsubscribe</div></div>
  </section>

  <footer class="footer">
    <span>© 2011 Tessaro Quinn Design Studios.</span>
    <span class="follow">Follow us&nbsp;&nbsp;<i></i><i></i></span>
  </footer>
</main>
</body>
</html>
```